Gutschein-Design für Bauträgerfirma
Sehr guter Designer, würde ich immer wieder weiter empfehlen.
Zielgruppe
Wir sind eine Bauträgerfirma und verkaufen Wohnungen für die gehobene Klasse.
Aufgabenstellung
Auflösung min. 150dpi, Format: 3,56m x 2,52m,
Dieses Banner soll eine Werbung bzw. einen Gutschein enthalten.
Folgender Text soll enthalten sein: Wenn Sie eine Wohnung bis zum 31.12.2018 bei uns kaufen, erhalten Sie einen Bemusterungsgutschein von 5.000€.
Der Text kann natürlich auch anders formuliert werden, der Kern sollte erhalten bleiben.
Die Unterlagen können auch im anderen Format zur Verfügung gestellt werden. Es sind alle Render in großem Format verfügbar.

```html
<!DOCTYPE html>
<html lang="de">
<head>
<meta charset="utf-8">
<title>Wohnresidenz am Lindenhang – Gutschein</title>
<link rel="stylesheet" href="https://fonts.googleapis.com/css2?family=Open+Sans:ital,wght@0,400;0,500;0,600;1,400&display=swap">
<style>
  :root{
    --backdrop:#a2a2a2;
    --navy:#172c52;
    --navy-panel:#1f3a68;
    --navy-fold:#0d1a34;
    --ink:#1b2a48;
    --white:#ffffff;
  }
  *{box-sizing:border-box;margin:0;padding:0}
  html,body{width:1088px;height:1200px;overflow:hidden;background:var(--backdrop)}
  body{position:relative;font-family:"Open Sans",sans-serif}
  .flyer{
    position:absolute;left:134px;top:20px;width:764px;height:1080px;
    background:var(--white);transform:scale(1.0741);transform-origin:0 0;overflow:hidden;
  }
  .brand{position:absolute;top:0;left:0;width:764px;height:138px;display:flex;align-items:center;justify-content:center;gap:10px}
  .brand-mark{width:16px;height:16px;background:var(--navy)}
  .brand-name{font-weight:600;font-size:22px;color:var(--navy);letter-spacing:.5px}
  .navy-band{position:absolute;left:0;top:138px;width:764px;height:842px;background:var(--navy)}
  .headline{position:absolute;top:178px;left:0;width:764px;text-align:center;color:var(--white);font-size:35px;font-weight:400;letter-spacing:1px}
  .rule{position:absolute;top:235px;left:259px;width:216px;height:1px;background:var(--white)}
  .subline{position:absolute;top:246px;left:0;width:764px;text-align:center;color:var(--white);font-size:22px;font-weight:600}
  .photo{position:absolute}
  .photo-exterior{left:0;top:308px;width:440px;height:400px;background:linear-gradient(180deg,#4f86c6 0%,#a9c7e4 35%,#e2e4e2 55%,#c9cfcc 68%,#6f9a45 85%,#4f7a32 100%)}
  .photo-kitchen{left:463px;top:308px;width:301px;height:208px;background:linear-gradient(160deg,#f2f2f0 0%,#dcdad6 55%,#a88b6a 100%)}
  .photo-living{left:463px;top:540px;width:301px;height:168px;background:linear-gradient(170deg,#9aa0a8 0%,#d9d7d2 55%,#8fb6b0 100%)}
  .feature-panel{position:absolute;left:28px;top:690px;width:708px;height:202px;background:var(--navy-panel);opacity:.97}
  .features{position:absolute;left:72px;top:732px;list-style:none;color:var(--white);font-style:italic;font-size:19.5px;line-height:29px}
  .features li::before{content:"•";display:inline-block;width:19px;font-style:normal;font-size:15px}
  .folds{position:absolute;left:0;top:0}
  .voucher{position:absolute;left:80px;top:878px;width:604px;height:120px;background:var(--white);box-shadow:0 6px 8px rgba(0,0,0,.25);
    display:flex;flex-direction:column;justify-content:center;text-align:center;color:var(--ink);font-size:19px;line-height:29px}
  .voucher strong{font-weight:600}
  .website{position:absolute;top:1014px;left:0;width:764px;text-align:center;color:var(--ink);font-size:31px;font-weight:500;letter-spacing:.3px}
</style>
</head>
<body>
  <article class="flyer">
    <header class="brand">
      <span class="brand-mark"></span>
      <span class="brand-name">HALVOR IMMOBILIEN</span>
    </header>
    <div class="navy-band"></div>
    <h1 class="headline">WOHNRESIDENZ AM LINDENHANG</h1>
    <div class="rule"></div>
    <p class="subline">Wohnen zum Wohlfühlen.</p>

    <div class="photo photo-exterior" role="img" aria-label="Außenansicht der Wohnanlage mit Terrassen und Rasenfläche"></div>
    <div class="photo photo-kitchen" role="img" aria-label="Innenansicht: offene Küche mit Essbereich"></div>
    <div class="photo photo-living" role="img" aria-label="Innenansicht: Wohnzimmer mit Sofa und Essplatz"></div>

    <div class="feature-panel"></div>
    <ul class="features">
      <li>19 Wohnungen , 2 bis 4 Zimmern , ca. 60 bis 160 Quadratmeter</li>
      <li>helle, freundliche und barrierefreie Bauweise</li>
      <li>besonders energieeffiziente KfW55 Häusern mit Blockheizkraftwerk</li>
      <li>attraktiver Spielplatz auf dem Gelände und Tiefgarage ...</li>
    </ul>

    <svg class="folds" width="764" height="1080" aria-hidden="true">
      <polygon points="58,980 80,980 80,998" fill="var(--navy-fold)"/>
      <polygon points="706,980 684,980 684,998" fill="var(--navy-fold)"/>
    </svg>
    <div class="voucher">
      <p>Kaufen Sie eine Wohnung bis zum <strong>31.12.2018</strong>,</p>
      <p>bedanken wir uns mit einem</p>
      <p>Bemusterungsgutschein im Wert von <strong>5.000 €</strong>.</p>
    </div>

    <p class="website">www.halvor-immobilien.com</p>
  </article>
</body>
</html>
```